Business Card Design Project

1. Show the company logo.
2. Only company email ID and website address to be shown (office@tikhayavolna.fm , www.tikhayavolna.fm).
3. Logo to be provided by us, 2 designs just in case. The logo is made with ' Tikhaya Volna' text, need to be edited so that it shows 'Yasnaya Afisha' instead .
4. Single sided business card, portrait or landscape is not a problem; back side to be filled with colors or a design that matches the logo the best.
5. Logo is to be embossed.
6. We're looking at an English and Russian version.
7. any other better idea is always welcomed.

```html
<!DOCTYPE html>
<html lang="en">
<head>
<meta charset="utf-8">
<title>Yasnaya Afisha — Business Card</title>
<link rel="stylesheet" href="https://fonts.googleapis.com/css2?family=Arimo:wght@400;700&display=swap">
<style>
  :root {
    --backdrop: #3a3a3b;
    --card: #222324;
    --card-edge: #1a1b1c;
    --badge-ring: #0c0c0d;
    --badge-fill: #1f4f9a;
    --pill-fill: #23407f;
    --pill-edge: #0b0b0c;
    --text-light: #f2f4f8;
    --mark-faint: #191a1b;
  }
  * { margin: 0; padding: 0; box-sizing: border-box; }
  html, body {
    width: 1200px;
    height: 534px;
    overflow: hidden;
    background: var(--backdrop);
    font-family: "Arimo", Arial, sans-serif;
  }
  .stage {
    position: relative;
    width: 1200px;
    height: 534px;
  }
  .card {
    position: absolute;
    top: 119px;
    width: 517px;
    height: 295px;
    background: var(--card);
    border: 1px solid var(--card-edge);
    box-shadow: 0 6px 14px rgba(0,0,0,0.45);
    overflow: hidden;
  }
  .card--front { left: 62px; }
  .card--back { left: 622px; }

  .badge {
    position: absolute;
    left: 173px;
    top: 20px;
    width: 170px;
    height: 170px;
    border-radius: 50%;
    background: var(--badge-fill);
    border: 8px solid var(--badge-ring);
    box-shadow: 0 3px 8px rgba(0,0,0,0.6);
    display: flex;
    align-items: center;
    justify-content: center;
    text-align: center;
  }
  .badge__name {
    color: var(--text-light);
    font-weight: 700;
    font-size: 19px;
    line-height: 1.15;
  }

  .contact {
    position: absolute;
    top: 244px;
    height: 30px;
    display: flex;
    align-items: center;
    gap: 7px;
    padding: 0 9px;
    background: var(--pill-fill);
    border: 3px solid var(--pill-edge);
    border-radius: 3px;
    color: var(--text-light);
    font-weight: 700;
    font-size: 15px;
    white-space: nowrap;
  }
  .contact--email { left: 21px; width: 255px; }
  .contact--web { left: 302px; width: 193px; }
  .contact__icon { width: 15px; height: 15px; flex: none; }

  .back-mark {
    position: absolute;
    left: -6px;
    top: 60px;
    color: var(--mark-faint);
    font-weight: 700;
    font-size: 96px;
    line-height: 0.95;
  }
</style>
</head>
<body>
<main class="stage">
  <section class="card card--front" aria-label="Business card front">
    <div class="badge">
      <span class="badge__name">Yasnaya<br>Afisha</span>
    </div>
    <div class="contact contact--email">
      <svg class="contact__icon" viewBox="0 0 16 16" aria-hidden="true">
        <rect x="1" y="3" width="14" height="10" fill="none" stroke="#f2f4f8" stroke-width="1.3"/>
        <path d="M1 3 L8 9 L15 3" fill="none" stroke="#f2f4f8" stroke-width="1.3"/>
      </svg>
      <span>office@tikhayavolna.fm</span>
    </div>
    <div class="contact contact--web">
      <svg class="contact__icon" viewBox="0 0 16 16" aria-hidden="true">
        <circle cx="8" cy="8" r="6.5" fill="none" stroke="#f2f4f8" stroke-width="1.2"/>
        <ellipse cx="8" cy="8" rx="3" ry="6.5" fill="none" stroke="#f2f4f8" stroke-width="1"/>
        <path d="M1.5 8 H14.5 M2.5 4.8 H13.5 M2.5 11.2 H13.5" stroke="#f2f4f8" stroke-width="1"/>
      </svg>
      <span>www.tikhayavolna.fm</span>
    </div>
  </section>

  <section class="card card--back" aria-label="Business card back">
    <div class="back-mark">Yasnaya<br>Afisha</div>
  </section>
</main>
</body>
</html>
```